Business Card Design Project

We are a commercial talent casting company, a very "now" company. We need a new business card that is both current, graphic and elegantly interesting. As we are a service business,
we need something that will attract the attention of new clients,
yet project a business that is 25 years old.

Industry/Entity Type

Business

Requirements
Must have
• 1. Logo - Nora Quillan Casting
2. Address - 47 Thornbury Street
New York, New York 10010
3. Phone - 212-738-4192
4. E-Mail - Casting@noraquillan.example

Nice to have
• Would like the card in black and white with the only accent
color being red.

```html
<!DOCTYPE html>
<html lang="en">
<head>
<meta charset="utf-8">
<title>Nora Quillan Casting — Business Card</title>
<link rel="stylesheet" href="https://fonts.googleapis.com/css2?family=Archivo+Black&family=Arimo:wght@400;700&display=swap">
<style>
  :root {
    --page: #d9d9d9;
    --card-top: #2b2b2b;
    --card-bottom: #121212;
    --ink: #ffffff;
    --ink-soft: #e6e6e6;
    --accent: #e0211b;
    --muted: #cfcfcf;
  }
  * { margin: 0; padding: 0; box-sizing: border-box; }
  html, body {
    width: 1200px; height: 951px; overflow: hidden;
    background: var(--page);
    font-family: "Arimo", Arial, sans-serif;
  }
  .canvas { position: relative; width: 1200px; height: 951px; }

  .card {
    position: absolute;
    width: 780px; height: 440px;
    border-radius: 34px;
    background: linear-gradient(160deg, var(--card-top), var(--card-bottom));
    box-shadow: 0 12px 30px rgba(0,0,0,0.35);
    overflow: hidden;
  }
  .card--front { left: 50px; top: 30px; }
  .card--back  { left: 380px; top: 490px; }

  /* Front */
  .wordmark {
    font-family: "Archivo Black", "Arial Black", sans-serif;
    color: var(--ink);
    text-transform: uppercase;
    line-height: 0.98;
  }
  .card--front .wordmark {
    position: absolute; left: 120px; top: 80px;
    font-size: 84px; letter-spacing: 1px;
  }
  .card--front .web {
    position: absolute; left: 180px; top: 362px;
    font-size: 21px; letter-spacing: 2.5px; color: var(--ink-soft);
  }

  /* Back */
  .stripe { position: absolute; top: 0; bottom: 0; }
  .stripe--line-left  { left: 58px;  width: 4px;  background: var(--muted); }
  .stripe--band       { left: 66px;  width: 38px; background: var(--accent); }
  .stripe--line-right { left: 108px; width: 4px;  background: var(--muted); }

  .person {
    position: absolute; left: 160px; top: 48px;
    font-size: 26px; letter-spacing: 2px; color: var(--ink);
    text-transform: uppercase;
  }
  .person .role {
    font-size: 17px; letter-spacing: 1px; color: var(--accent);
    text-transform: none; margin-left: 6px;
  }

  .contact {
    position: absolute; left: 160px;
    font-size: 20px; line-height: 1.3; color: var(--ink-soft);
    list-style: none;
  }
  .contact--address { top: 172px; }
  .contact--lines { top: 300px; }
  .contact li { display: flex; align-items: flex-start; gap: 12px; }
  .contact svg { flex: none; width: 18px; height: 18px; margin-top: 3px; fill: var(--ink-soft); }

  .card--back .wordmark {
    position: absolute; right: 60px; bottom: 58px;
    font-size: 44px; letter-spacing: 1px; text-align: left;
  }
</style>
</head>
<body>
<main class="canvas">

  <section class="card card--front" aria-label="Card front">
    <h1 class="wordmark">Nora<br>Quillan<br>Casting</h1>
    <p class="web">www.noraquillan.example</p>
  </section>

  <section class="card card--back" aria-label="Card back">
    <div class="stripe stripe--line-left"></div>
    <div class="stripe stripe--band"></div>
    <div class="stripe stripe--line-right"></div>

    <p class="person">Marcus Delane <span class="role">director</span></p>

    <ul class="contact contact--address">
      <li>
        <svg viewBox="0 0 20 20" aria-hidden="true"><path d="M10 2 1 10h3v8h5v-5h2v5h5v-8h3z"/></svg>
        <span>47 Thornbury Street<br>New York,<br>New York 10010</span>
      </li>
    </ul>

    <ul class="contact contact--lines">
      <li>
        <svg viewBox="0 0 20 20" aria-hidden="true"><path d="M5 2h3l1.5 4-2 1.5a10 10 0 0 0 5 5l1.5-2 4 1.5v3a2 2 0 0 1-2 2A15 15 0 0 1 3 4a2 2 0 0 1 2-2z"/></svg>
        <span>212-738-4192</span>
      </li>
      <li>
        <svg viewBox="0 0 20 20" aria-hidden="true"><path d="M2 5h16v10H2zm1.5 1.2v.4L10 11l6.5-4.4v-.4z"/></svg>
        <span>casting@noraquillan.example</span>
      </li>
      <li>
        <svg viewBox="0 0 20 20" aria-hidden="true"><circle cx="10" cy="10" r="8"/></svg>
        <span>www.noraquillan.example</span>
      </li>
    </ul>

    <p class="wordmark">Nora<br>Quillan<br>Casting</p>
  </section>

</main>
</body>
</html>
```